Dinewell - Tablet App Design Project

I have a Tablet app that serves as a restaurant reservation system. The design that i currently have is very basic apple design. I am looking for it to have a much more professional appeal.

Please review the attached document which contains all of the screen shots for the app.
Updates

This Project has now been Guaranteed.  I look forward to reviewing your designs.

Brent

Reason: I am extending my deadline because i just changed this contest to guaranteed and have received a ton more "acceptances" because of it and I want to give those designers a chance to submit a design.

Target Market(s)

restaurant owners

Industry/Entity Type

Restaurant

Requirements
Must have
• On the seating chart i am changing the feature that shows the tables highlighted and instead would like that replace with a badge. So the list of wait staff across the top of the seating chart would instead have a number next to their name and would correspond with the badge on the table to determine their section.

So for example:
Ada would have a number 1 in front of her name and tables 18, 19, 20, and 31 would have a little badge in the upper right hand corner with the number "1" inside the badge.
Uma would have a number 2 in front of her name and tables 6, 7, and 11 would have a little badge in the upper right hand corner with the number " 2" inside the badge.
Nora would have a number 3 in front of her name and tables 12, 13, 27, 28, 29, and 30 would have a little badge in the upper right hand corner with the number " 3" inside the badge.

The names on the top will all be ONE color

Also, i would like an icon developed to replace the "C" you see next to some of the people's name in the reservation and waitlist slots. Also, i would like a better looking "check mark".

```html
<!DOCTYPE html>
<html lang="en">
<head>
<meta charset="utf-8">
<title>Dinewell – tablet reservation app</title>
<link href="https://fonts.googleapis.com/css2?family=Arimo:wght@400;700&display=swap" rel="stylesheet">
<style>
:root{
  --page:#ffffff;
  --brand:#4a9be0;
  --caption:#555555;
  --status:#111111;
  --toolbar:#3b3b3b;
  --toolbar-line:#1c1c1c;
  --infobar:#2c2c2c;
  --body:#d8d5ce;
  --panel:#3a3a3a;
  --panel-line:#6a6a6a;
  --waitlist-head:#3f7fbf;
  --slot-head:#c8a54a;
  --btn-top:#8a8a8a;
  --btn-bottom:#4d4d4d;
  --text:#ffffff;
  --muted:#a9a9a9;
  --late:#e8392c;
  --soon:#f08a2a;
  --check:#4cc24a;
  --floor:#3c3c3c;
  --table:#f4f4f4;
  --table-num:#8c8c8c;
  --s1:#c0281e;--s2:#58b22a;--s3:#1c2fbf;--s4:#c8571a;--s5:#4a2ab8;
  --s6:#1ea3b5;--s7:#a9b41e;--s8:#9a9a9a;--s9:#8db21e;
}
*{box-sizing:border-box;margin:0;padding:0}
html,body{width:1200px;height:628px;overflow:hidden;background:var(--page);font-family:"Arimo",Helvetica,Arial,sans-serif;color:var(--text)}
.board{position:relative;width:1200px;height:628px}
.brand{position:absolute;left:88px;top:32px}
.brand-name{font-size:20px;font-weight:700;letter-spacing:1.5px;color:var(--brand)}
.brand-sub{font-size:6.5px;color:var(--caption);margin-top:4px;margin-left:10px}
.screen{position:absolute;top:94px;width:476px;height:364px;background:var(--body);overflow:hidden}
.screen-1{left:86px}
.screen-2{left:632px}
.caption{position:absolute;top:465px;font-size:6.5px;letter-spacing:.6px;color:var(--caption);width:476px;text-align:center}
.caption-1{left:86px}.caption-2{left:632px}

.statusbar{height:10px;background:var(--status);display:flex;justify-content:space-between;align-items:center;padding:0 5px;font-size:7px;color:#ddd}
.battery{width:12px;height:5px;border:1px solid #ddd;position:relative}
.battery::after{content:"";position:absolute;inset:1px;background:#ddd}
.toolbar{height:24px;background:var(--toolbar);border-bottom:1px solid var(--toolbar-line);display:flex;align-items:center;padding:0 5px;gap:4px;position:relative}
.btn{font-size:6.5px;padding:4px 4px;border-radius:3px;background:linear-gradient(var(--btn-top),var(--btn-bottom));border:1px solid #222;color:#fff;white-space:nowrap}
.toolbar .spacer{flex:1}
.toolbar-title{position:absolute;left:50%;transform:translateX(-50%);font-size:10px;font-weight:700;letter-spacing:1px;color:var(--brand)}

.infobar{height:32px;background:var(--infobar);display:flex;align-items:center;padding:0 6px}
.clock{font-size:15px;font-weight:700;margin-right:3px}
.date{font-size:5px;line-height:1.25;margin-right:6px}
.stat{border-left:1px dotted #888;padding:0 5px;height:24px;display:flex;flex-direction:column;justify-content:center}
.stat-label{font-size:6px;color:#ddd}
.stat-value{font-size:9.5px;font-weight:700;margin-top:2px}

.panel{position:absolute;background:var(--panel);box-shadow:0 1px 2px rgba(0,0,0,.4);overflow:hidden}
.panel-head{height:14px;display:flex;align-items:center;padding:0 5px;font-size:7px;font-weight:700}
.waitlist .panel-head{background:var(--waitlist-head)}
.add-party{height:22px;display:flex;align-items:center;gap:5px;padding:0 9px;font-size:6.5px;border-bottom:1px dotted var(--panel-line)}
.plus{width:10px;height:10px;border:1px solid #fff;border-radius:50%;position:relative}
.plus::before,.plus::after{content:"";position:absolute;background:#fff;left:50%;top:50%;transform:translate(-50%,-50%)}
.plus::before{width:6px;height:1px}.plus::after{width:1px;height:6px}
.guest{height:26px;display:flex;justify-content:space-between;align-items:center;padding:0 9px;border-bottom:1px dotted var(--panel-line)}
.screen-2 .guest{height:25px}
.guest-name{font-size:7px;font-weight:700}
.guest-party{font-size:5.5px;font-style:italic;color:#ccc;font-weight:400;display:block;margin-top:1px}
.guest-wait{font-size:7px}
.late{color:var(--late)}.soon{color:var(--soon)}

.slot{position:absolute;background:var(--panel);box-shadow:0 1px 2px rgba(0,0,0,.4);overflow:hidden}
.slot-head{height:14px;background:var(--slot-head);display:flex;align-items:center;padding:0 5px;font-size:7px;font-weight:700}
.slot-head .count{margin-left:14px}
.slot-head .count.full{color:var(--late)}
.slot-head .size{margin-left:auto;margin-right:4px}
.slot-head .add{font-size:10px;line-height:1}
.booking{display:grid;grid-template-columns:1fr 20px 12px 14px;align-items:center;height:15px;padding-left:5px;margin-top:2px}
.booking-name{font-size:6.2px;font-weight:700;white-space:nowrap}
.booking-name.arrived{color:var(--muted);font-weight:400}
.booking-note{display:block;font-size:4.4px;font-style:italic;font-weight:700;color:#ddd;margin-top:1px;white-space:nowrap}
.booking-name.arrived .booking-note{color:#aaa;font-weight:400}
.marks{display:flex;gap:2px;justify-content:flex-end;align-items:center}
.booking-size,.booking-table{font-size:6px;text-align:center}
.booking-table{border-left:1px dotted #888;height:100%;display:flex;align-items:center;justify-content:center}
.booking-size{color:#ddd}

.check{display:inline-block;width:3px;height:6px;border:solid var(--check);border-width:0 2px 2px 0;transform:rotate(40deg);margin:0 2px 2px}
.note-icon{display:inline-block;width:7px;height:5px;background:#e6e6e6;position:relative;overflow:hidden}
.note-icon::after{content:"";position:absolute;left:1px;top:-3px;width:4px;height:4px;border:1px solid #777;transform:rotate(45deg)}

.key{position:absolute;left:86px;top:503px;width:248px;height:92px;background:#474747;padding:8px 8px}
.key-title{font-size:7px;font-weight:700;padding-bottom:4px;border-bottom:1px dotted #bbb}
.key-row{display:flex;align-items:center;gap:14px;font-size:7px;margin-top:8px;padding-left:4px}
.key-row .mark{width:8px;display:flex;justify-content:center}

.staff{height:32px;background:var(--infobar);display:flex;align-items:center;gap:11px;padding:0 8px;font-size:7.5px;font-weight:700}
.staff-item{display:flex;align-items:center;gap:4px;color:var(--text)}
.badge{display:inline-flex;align-items:center;justify-content:center;width:10px;height:10px;border-radius:2px;font-size:6.5px;font-weight:700;color:#fff}
.b1{background:var(--s1)}.b2{background:var(--s2)}.b3{background:var(--s3)}.b4{background:var(--s4)}.b5{background:var(--s5)}
.b6{background:var(--s6)}.b7{background:var(--s7)}.b8{background:var(--s8)}.b9{background:var(--s9)}
.floor{position:absolute;left:162px;top:73px;width:305px;height:290px;background:var(--floor)}
.floor text{font-family:"Arimo",Helvetica,Arial,sans-serif}
.tbl{fill:var(--table)}
.tnum{fill:var(--table-num);font-size:11px;font-weight:700;text-anchor:middle;dominant-baseline:central}
.bnum{fill:#fff;font-size:6.5px;font-weight:700;text-anchor:middle;dominant-baseline:central}
</style>
</head>
<body>
<div class="board">

  <div class="brand">
    <div class="brand-name">DINEWELL</div>
    <div class="brand-sub">Tablet application</div>
  </div>

  <!-- Reservations screen -->
  <section class="screen screen-1">
    <div class="statusbar"><span>Tablet</span><span>2:17 PM</span><span class="battery"></span></div>
    <div class="toolbar">
      <span class="btn">Seating</span><span class="btn">Specials</span><span class="btn">Notes</span>
      <span class="toolbar-title">DINEWELL</span>
      <span class="spacer"></span>
      <span class="btn">Calendar</span><span class="btn">Manage</span>
    </div>
    <div class="infobar">
      <span class="clock">2:17 PM</span>
      <span class="date">Monday<br>September 10th</span>
      <div class="stat"><span class="stat-label">Avg Wait</span><span class="stat-value">25 mins</span></div>
      <div class="stat"><span class="stat-label">Open Tables</span><span class="stat-value">66</span></div>
      <div class="stat"><span class="stat-label">Checked In</span><span class="stat-value">14 Groups - 56 People</span></div>
      <div class="stat"><span class="stat-label">Currently Seated</span><span class="stat-value">11/296</span></div>
      <div class="stat"><span class="stat-label">Open Reservations</span><span class="stat-value">370 People</span></div>
    </div>

    <div class="panel waitlist" style="left:6px;top:72px;width:153px;height:284px">
      <div class="panel-head">Wait List</div>
      <div class="add-party"><span class="plus"></span>Add party to wait list</div>
      <div class="guest"><span class="guest-name">Clara Benton<span class="guest-party">Party of 4</span></span><span class="guest-wait late">5m (2:02 PM)</span></div>
      <div class="guest"><span class="guest-name">Brent Hollis<span class="guest-party">Party of 2</span></span><span class="guest-wait late">5m (2:02 PM)</span></div>
      <div class="guest"><span class="guest-name">Rosa Finn<span class="guest-party">Party of 4</span></span><span class="guest-wait">25m (2:22 PM)</span></div>
      <div class="guest"><span class="guest-name">Marisol Vega<span class="guest-party">Party of 3</span></span><span class="guest-wait">25m (2:23 PM)</span></div>
      <div class="guest"><span class="guest-name">Hannah Okafor<span class="guest-party">Party of 4</span></span><span class="guest-wait">30m (2:28 PM)</span></div>
      <div class="guest"><span class="guest-name">Greta Lund<span class="guest-party">Party of 6</span></span><span class="guest-wait">30m (2:28 PM)</span></div>
      <div class="guest"><span class="guest-name">Nina Sorel<span class="guest-party">Party of 6</span></span><span class="guest-wait">30m (2:28 PM)</span></div>
      <div class="guest"><span class="guest-name">Yvonne Castell<span class="guest-party">Party of 4</span></span><span class="guest-wait soon">15m (2:14 PM)</span></div>
      <div class="guest"><span class="guest-name">Peter Lowe<span class="guest-party">Party of 4</span></span><span class="guest-wait">40m (2:39 PM)</span></div>
    </div>

    <div class="slot" style="left:163px;top:72px;width:151px;height:66px">
      <div class="slot-head">12:00 PM<span class="count">9/22</span><span class="size">Size</span><span class="add">+</span></div>
      <div class="booking"><span class="booking-name arrived">Carl Webb<span class="booking-note">I would like a booth in the corner</span></span><span class="marks"><i class="check"></i></span><span class="booking-size">4</span><span class="booking-table">11</span></div>
      <div class="booking"><span class="booking-name">Ada Quill</span><span class="marks"><i class="check"></i></span><span class="booking-size">3</span><span class="booking-table"></span></div>
      <div class="booking"><span class="booking-name arrived">Victor Ames<span class="booking-note">Patio table if available</span></span><span class="marks"><i class="note-icon"></i></span><span class="booking-size">2</span><span class="booking-table">1</span></div>
    </div>
    <div class="slot" style="left:163px;top:142px;width:151px;height:81px">
      <div class="slot-head">12:15 PM<span class="count full">Full</span><span class="size">Size</span><span class="add">+</span></div>
      <div class="booking"><span class="booking-name">Dean Foster</span><span class="marks"><i class="check"></i></span><span class="booking-size">4</span><span class="booking-table"></span></div>
      <div class="booking"><span class="booking-name">Luke Marsh<span class="booking-note">Birthday celebration</span></span><span class="marks"><i class="note-icon"></i><i class="check"></i></span><span class="booking-size">2</span><span class="booking-table">12</span></div>
      <div class="booking"><span class="booking-name">Raul Denby<span class="booking-note">We have one person who needs gluten free food</span></span><span class="marks"><i class="check"></i></span><span class="booking-size">2</span><span class="booking-table">1</span></div>
      <div class="booking"><span class="booking-name">Ian Whitlock</span><span class="marks"></span><span class="booking-size">4</span><span class="booking-table"></span></div>
    </div>
    <div class="slot" style="left:163px;top:227px;width:151px;height:66px">
      <div class="slot-head">12:30 PM<span class="count">12/20</span><span class="size">Size</span><span class="add">+</span></div>
      <div class="booking"><span class="booking-name">Mabel Crane</span><span class="marks"><i class="check"></i></span><span class="booking-size">4</span><span class="booking-table"></span></div>
      <div class="booking"><span class="booking-name">Sara Wilde</span><span class="marks"><i class="check"></i></span><span class="booking-size">4</span><span class="booking-table"></span></div>
      <div class="booking"><span class="booking-name">Harold Pike<span class="booking-note">Corner Booth</span></span><span class="marks"><i class="note-icon"></i></span><span class="booking-size">2</span><span class="booking-table">12</span></div>
    </div>
    <div class="slot" style="left:163px;top:298px;width:151px;height:45px">
      <div class="slot-head">12:45 PM<span class="count">7/20</span><span class="size">Size</span><span class="add">+</span></div>
      <div class="booking"><span class="booking-name">Eli Burke</span><span class="marks"></span><span class="booking-size">3</span><span class="booking-table"></span></div>
      <div class="booking"><span class="booking-name">Felix Rowan</span><span class="marks"><i class="note-icon"></i></span><span class="booking-size">4</span><span class="booking-table"></span></div>
    </div>

    <div class="slot" style="left:318px;top:72px;width:151px;height:82px">
      <div class="slot-head">1:00 PM<span class="count full">Full</span><span class="size">Size</span><span class="add">+</span></div>
      <div class="booking"><span class="booking-name">Maya Lenz<span class="booking-note">Quiet table in back</span></span><span class="marks"><i class="note-icon"></i></span><span class="booking-size">2</span><span class="booking-table"></span></div>
      <div class="booking"><span class="booking-name">Irene Castor</span><span class="marks"></span><span class="booking-size">4</span><span class="booking-table"></span></div>
      <div class="booking"><span class="booking-name">Molly Grant<span class="booking-note">Booth please</span></span><span class="marks"><i class="note-icon"></i></span><span class="booking-size">3</span><span class="booking-table"></span></div>
      <div class="booking"><span class="booking-name">Edith Moss</span><span class="marks"></span><span class="booking-size">4</span><span class="booking-table"></span></div>
    </div>
    <div class="slot" style="left:318px;top:158px;width:151px;height:65px">
      <div class="slot-head">1:15 PM<span class="count">17/20</span><span class="size">Size</span><span class="add">+</span></div>
      <div class="booking"><span class="booking-name">Ada Renner</span><span class="marks"></span><span class="booking-size">5</span><span class="booking-table"></span></div>
      <div class="booking"><span class="booking-name">Simon Hart<span class="booking-note">Business meeting</span></span><span class="marks"></span><span class="booking-size">8</span><span class="booking-table"></span></div>
      <div class="booking"><span class="booking-name">Neil Garza</span><span class="marks"><i class="note-icon"></i></span><span class="booking-size">4</span><span class="booking-table"></span></div>
    </div>
    <div class="slot" style="left:318px;top:227px;width:151px;height:80px">
      <div class="slot-head">1:30 PM<span class="count full">Full</span><span class="size">Size</span><span class="add">+</span></div>
      <div class="booking"><span class="booking-name">Ray Dobson</span><span class="marks"></span><span class="booking-size">6</span><span class="booking-table"></span></div>
      <div class="booking"><span class="booking-name">Colin Barrett<span class="booking-note">Patio please</span></span><span class="marks"><i class="note-icon"></i></span><span class="booking-size">2</span><span class="booking-table"></span></div>
      <div class="booking"><span class="booking-name">Beatrice Harlow</span><span class="marks"></span><span class="booking-size">6</span><span class="booking-table"></span></div>
      <div class="booking"><span class="booking-name">Gus Weller</span><span class="marks"><i class="note-icon"></i></span><span class="booking-size">2</span><span class="booking-table"></span></div>
    </div>
    <div class="slot" style="left:318px;top:311px;width:151px;height:36px">
      <div class="slot-head">12:45 PM<span class="count">4/20</span><span class="size">Size</span><span class="add">+</span></div>
      <div class="booking"><span class="booking-name"></span><span class="marks"></span><span class="booking-size"></span><span class="booking-table" style="height:18px"></span></div>
    </div>
  </section>
  <div class="caption caption-1">SCREEN 1</div>

  <!-- Seating chart screen -->
  <section class="screen screen-2">
    <div class="statusbar"><span>Tablet</span><span>1:16 PM</span><span class="battery"></span></div>
    <div class="toolbar">
      <span class="btn">Home</span><span class="btn">Edit Floor</span>
      <span class="toolbar-title">DINEWELL</span>
      <span class="spacer"></span>
      <span class="btn">Manage Sections</span><span class="btn">Select Floor</span>
    </div>
    <div class="staff">
      <span class="staff-item"><span class="badge b1">1</span>Ada</span>
      <span class="staff-item"><span class="badge b2">2</span>Uma</span>
      <span class="staff-item"><span class="badge b3">3</span>Nora</span>
      <span class="staff-item"><span class="badge b4">4</span>Iris</span>
      <span class="staff-item"><span class="badge b5">5</span>Theo</span>
      <span class="staff-item"><span class="badge b6">6</span>Lena</span>
      <span class="staff-item"><span class="badge b7">7</span>Owen</span>
      <span class="staff-item"><span class="badge b8">8</span>Paul</span>
      <span class="staff-item"><span class="badge b9">9</span>Ada</span>
    </div>

    <div class="panel waitlist" style="left:6px;top:72px;width:150px;height:137px">
      <div class="panel-head">Wait List</div>
      <div class="add-party"><span class="plus"></span>Add party to wait list</div>
      <div class="guest"><span class="guest-name">Clara Benton<span class="guest-party">Party of 4</span></span><span class="guest-wait late">5m (2:02 PM)</span></div>
      <div class="guest"><span class="guest-name">Brent Hollis<span class="guest-party">Party of 2</span></span><span class="guest-wait late">5m (2:02 PM)</span></div>
      <div class="guest"><span class="guest-name">Rosa Finn<span class="guest-party">Party of 4</span></span><span class="guest-wait soon">15m (1:21 PM)</span></div>
      <div class="guest"><span class="guest-name">Marisol Vega<span class="guest-party">Party of 3</span></span><span class="guest-wait soon">15m (1:21 PM)</span></div>
    </div>
    <div class="slot" style="left:6px;top:212px;width:150px;height:50px">
      <div class="slot-head">12:00 PM<span class="count">7/22</span><span class="size">Size</span><span class="add">+</span></div>
      <div class="booking"><span class="booking-name">Carl Webb<span class="booking-note">I would like a booth in the corner</span></span><span class="marks"><i class="check"></i></span><span class="booking-size">4</span><span class="booking-table"></span></div>
      <div class="booking"><span class="booking-name">Ada Quill</span><span class="marks"><i class="check"></i></span><span class="booking-size">3</span><span class="booking-table"></span></div>
    </div>
    <div class="slot" style="left:6px;top:265px;width:150px;height:66px">
      <div class="slot-head">12:15 PM<span class="count">11/20</span><span class="size">Size</span><span class="add">+</span></div>
      <div class="booking"><span class="booking-name">Dean Foster</span><span class="marks"><i class="check"></i></span><span class="booking-size">4</span><span class="booking-table"></span></div>
      <div class="booking"><span class="booking-name">Luke Marsh<span class="booking-note">Birthday celebration</span></span><span class="marks"><i class="note-icon"></i><i class="check"></i></span><span class="booking-size">2</span><span class="booking-table"></span></div>
      <div class="booking"><span class="booking-name">Raul Denby<span class="booking-note">We have one person who needs gluten free food</span></span><span class="marks"><i class="check"></i></span><span class="booking-size">2</span><span class="booking-table"></span></div>
    </div>
    <div class="slot" style="left:6px;top:334px;width:150px;height:31px">
      <div class="slot-head">12:30 PM<span class="count">9/20</span><span class="size">Size</span><span class="add">+</span></div>
      <div class="booking" style="margin-top:1px"><span class="booking-name">Mabel Crane</span><span class="marks"><i class="check"></i></span><span class="booking-size">4</span><span class="booking-table"></span></div>
    </div>

    <svg class="floor" viewBox="0 0 305 290" role="img" aria-label="Floor plan with tables and server section badges">
      <g>
        <circle class="tbl" cx="30" cy="30" r="22"/><text class="tnum" x="30" y="30">1</text>
        <circle class="tbl" cx="30" cy="85" r="22"/><text class="tnum" x="30" y="85">2</text>
        <circle class="tbl" cx="30" cy="140" r="22"/><text class="tnum" x="30" y="140">3</text>
        <circle class="tbl" cx="30" cy="194" r="22"/><text class="tnum" x="30" y="194">4</text>
        <circle class="tbl" cx="30" cy="248" r="22"/><text class="tnum" x="30" y="248">5</text>
      </g>
      <g>
        <rect class="tbl" x="66" y="9" width="42" height="42"/><text class="tnum" x="87" y="30">6</text>
        <rect class="tbl" x="66" y="64" width="42" height="42"/><text class="tnum" x="87" y="85">7</text>
        <rect class="tbl" x="66" y="117" width="42" height="44"/><text class="tnum" x="87" y="139">8</text>
        <rect class="tbl" x="66" y="173" width="42" height="43"/><text class="tnum" x="87" y="194">9</text>
        <rect class="tbl" x="66" y="226" width="42" height="44"/><text class="tnum" x="87" y="248">10</text>
        <rect class="tbl" x="119" y="9" width="60" height="42"/><text class="tnum" x="149" y="30">11</text>
        <rect class="tbl" x="188" y="9" width="60" height="42"/><text class="tnum" x="218" y="30">12</text>
        <rect class="tbl" x="255" y="9" width="44" height="42"/><text class="tnum" x="277" y="30">13</text>
        <rect class="tbl" x="123" y="63" width="19" height="52"/><text class="tnum" x="132.5" y="89">18</text>
        <rect class="tbl" x="154" y="63" width="18" height="52"/><text class="tnum" x="163" y="89">19</text>
        <rect class="tbl" x="186" y="63" width="18" height="52"/><text class="tnum" x="195" y="89">20</text>
        <rect class="tbl" x="227" y="63" width="18" height="18"/><text class="tnum" x="236" y="72">27</text>
        <rect class="tbl" x="260" y="63" width="18" height="18"/><text class="tnum" x="269" y="72">29</text>
        <rect class="tbl" x="227" y="94" width="18" height="17"/><text class="tnum" x="236" y="102.5">28</text>
        <rect class="tbl" x="260" y="94" width="18" height="17"/><text class="tnum" x="269" y="102.5">30</text>
        <rect class="tbl" x="242" y="134" width="57" height="52"/><text class="tnum" x="270.5" y="160">31</text>
        <rect class="tbl" x="119" y="198" width="52" height="18"/><text class="tnum" x="145" y="207">21</text>
        <rect class="tbl" x="189" y="198" width="47" height="18"/><text class="tnum" x="212.5" y="207">26</text>
        <rect class="tbl" x="244" y="198" width="52" height="18"/><text class="tnum" x="270" y="207">36</text>
      </g>
      <g>
        <rect class="tbl" x="-8" y="-8" width="16" height="16" transform="translate(134 145) rotate(45)"/><text class="tnum" x="134" y="145">22</text>
        <rect class="tbl" x="-8" y="-8" width="16" height="16" transform="translate(164 145) rotate(45)"/><text class="tnum" x="164" y="145">23</text>
        <rect class="tbl" x="-8" y="-8" width="16" height="16" transform="translate(134 174) rotate(45)"/><text class="tnum" x="134" y="174">24</text>
        <rect class="tbl" x="-8" y="-8" width="16" height="16" transform="translate(164 174) rotate(45)"/><text class="tnum" x="164" y="174">25</text>
        <circle class="tbl" cx="196" cy="145" r="11"/><text class="tnum" x="196" y="145">32</text>
        <circle class="tbl" cx="222" cy="145" r="11"/><text class="tnum" x="222" y="145">33</text>
        <circle class="tbl" cx="196" cy="174" r="11"/><text class="tnum" x="196" y="174">34</text>
        <circle class="tbl" cx="222" cy="174" r="11"/><text class="tnum" x="222" y="174">35</text>
      </g>
      <g>
        <rect class="tbl" x="-16" y="-16" width="32" height="32" transform="translate(141 248) rotate(45)"/><text class="tnum" x="141" y="248">14</text>
        <rect class="tbl" x="-16" y="-16" width="32" height="32" transform="translate(186 248) rotate(45)"/><text class="tnum" x="186" y="248">15</text>
        <rect class="tbl" x="-16" y="-16" width="32" height="32" transform="translate(230 248) rotate(45)"/><text class="tnum" x="230" y="248">16</text>
        <rect class="tbl" x="-16" y="-16" width="32" height="32" transform="translate(276 248) rotate(45)"/><text class="tnum" x="276" y="248">17</text>
      </g>
      <g>
        <rect x="43" y="4" width="10" height="10" rx="2" fill="var(--s4)"/><text class="bnum" x="48" y="9">4</text>
        <rect x="43" y="59" width="10" height="10" rx="2" fill="var(--s4)"/><text class="bnum" x="48" y="64">4</text>
        <rect x="43" y="114" width="10" height="10" rx="2" fill="var(--s4)"/><text class="bnum" x="48" y="119">4</text>
        <rect x="43" y="168" width="10" height="10" rx="2" fill="var(--s4)"/><text class="bnum" x="48" y="173">4</text>
        <rect x="43" y="222" width="10" height="10" rx="2" fill="var(--s6)"/><text class="bnum" x="48" y="227">6</text>
        <rect x="100" y="4" width="10" height="10" rx="2" fill="var(--s2)"/><text class="bnum" x="105" y="9">2</text>
        <rect x="100" y="59" width="10" height="10" rx="2" fill="var(--s2)"/><text class="bnum" x="105" y="64">2</text>
        <rect x="100" y="112" width="10" height="10" rx="2" fill="var(--s6)"/><text class="bnum" x="105" y="117">6</text>
        <rect x="100" y="168" width="10" height="10" rx="2" fill="var(--s6)"/><text class="bnum" x="105" y="173">6</text>
        <rect x="100" y="221" width="10" height="10" rx="2" fill="var(--s6)"/><text class="bnum" x="105" y="226">6</text>
        <rect x="172" y="4" width="10" height="10" rx="2" fill="var(--s2)"/><text class="bnum" x="177" y="9">2</text>
        <rect x="241" y="4" width="10" height="10" rx="2" fill="var(--s3)"/><text class="bnum" x="246" y="9">3</text>
        <rect x="292" y="4" width="10" height="10" rx="2" fill="var(--s3)"/><text class="bnum" x="297" y="9">3</text>
        <rect x="135" y="58" width="10" height="10" rx="2" fill="var(--s1)"/><text class="bnum" x="140" y="63">1</text>
        <rect x="165" y="58" width="10" height="10" rx="2" fill="var(--s1)"/><text class="bnum" x="170" y="63">1</text>
        <rect x="197" y="58" width="10" height="10" rx="2" fill="var(--s1)"/><text class="bnum" x="202" y="63">1</text>
        <rect x="239" y="58" width="10" height="10" rx="2" fill="var(--s3)"/><text class="bnum" x="244" y="63">3</text>
        <rect x="272" y="58" width="10" height="10" rx="2" fill="var(--s3)"/><text class="bnum" x="277" y="63">3</text>
        <rect x="239" y="89" width="10" height="10" rx="2" fill="var(--s3)"/><text class="bnum" x="244" y="94">3</text>
        <rect x="272" y="89" width="10" height="10" rx="2" fill="var(--s3)"/><text class="bnum" x="277" y="94">3</text>
        <rect x="292" y="129" width="10" height="10" rx="2" fill="var(--s1)"/><text class="bnum" x="297" y="134">1</text>
        <rect x="136" y="130" width="10" height="10" rx="2" fill="var(--s7)"/><text class="bnum" x="141" y="135">7</text>
        <rect x="166" y="130" width="10" height="10" rx="2" fill="var(--s7)"/><text class="bnum" x="171" y="135">7</text>
        <rect x="136" y="159" width="10" height="10" rx="2" fill="var(--s7)"/><text class="bnum" x="141" y="164">7</text>
        <rect x="166" y="159" width="10" height="10" rx="2" fill="var(--s7)"/><text class="bnum" x="171" y="164">7</text>
        <rect x="201" y="130" width="10" height="10" rx="2" fill="var(--s7)"/><text class="bnum" x="206" y="135">7</text>
        <rect x="227" y="130" width="10" height="10" rx="2" fill="var(--s5)"/><text class="bnum" x="232" y="135">5</text>
        <rect x="201" y="159" width="10" height="10" rx="2" fill="var(--s5)"/><text class="bnum" x="206" y="164">5</text>
        <rect x="227" y="159" width="10" height="10" rx="2" fill="var(--s5)"/><text class="bnum" x="232" y="164">5</text>
        <rect x="163" y="193" width="10" height="10" rx="2" fill="var(--s9)"/><text class="bnum" x="168" y="198">9</text>
        <rect x="228" y="193" width="10" height="10" rx="2" fill="var(--s9)"/><text class="bnum" x="233" y="198">9</text>
        <rect x="288" y="193" width="10" height="10" rx="2" fill="var(--s8)"/><text class="bnum" x="293" y="198">8</text>
        <rect x="145" y="228" width="10" height="10" rx="2" fill="var(--s9)"/><text class="bnum" x="150" y="233">9</text>
        <rect x="190" y="228" width="10" height="10" rx="2" fill="var(--s9)"/><text class="bnum" x="195" y="233">9</text>
        <rect x="234" y="228" width="10" height="10" rx="2" fill="var(--s8)"/><text class="bnum" x="239" y="233">8</text>
        <rect x="280" y="228" width="10" height="10" rx="2" fill="var(--s8)"/><text class="bnum" x="285" y="233">8</text>
      </g>
    </svg>
  </section>
  <div class="caption caption-2">SCREEN 2</div>

  <div class="key">
    <div class="key-title">KEY</div>
    <div class="key-row"><span class="mark"><i class="note-icon"></i></span>Customer note</div>
    <div class="key-row"><span class="mark"><i class="check"></i></span>Check-In</div>
  </div>

</div>
</body>
</html>
```